Billboard design 8x3M LUMA (Spanish company)

We´re located in the south of Spain. We run a local telecom company.
We sell Fiber optic, and mobile phone lines mainly.
The billboard will have to be in Spanish, I would like the price to be something you spot on first sight when passing by in the car.
Our company color is blue, like in our logo which I will add. I will also add a example from what we currently have.
The new offer should be:
1000 megas + 100Gigas movil con llamadas ilimitadas. (meaning 1000Mb fiber optic speed and 100Gb data and unlimited calls for 1 mobile line)
Our details are: phone line 956 47 8092
Website: lu-ma.es

```html
<!DOCTYPE html>
<html lang="es">
<head>
<meta charset="utf-8">
<title>LUMA – Valla 8x3</title>
<link href="https://fonts.googleapis.com/css2?family=Montserrat:wght@700;800;900&family=Barlow+Semi+Condensed:wght@600;700&display=swap" rel="stylesheet">
<style>
  :root {
    --page-bg: #e8edf6;
    --brand-blue: #0b2f9a;
    --deep-blue: #06207a;
    --band-blue: #0a2c8f;
    --glow-blue: #2f8cff;
    --cyan: #7fd0ff;
    --price-yellow: #ffd21a;
    --white: #ffffff;
  }
  * { margin: 0; padding: 0; box-sizing: border-box; }
  html, body {
    width: 1200px; height: 800px; overflow: hidden;
    background: var(--page-bg);
  }
  .canvas {
    width: 1200px; height: 800px;
    display: flex; align-items: center; justify-content: center;
  }
  .billboard {
    position: relative;
    width: 1200px; height: 527px;
    background:
      radial-gradient(ellipse 45% 60% at 78% 52%, rgba(80,170,255,.55), transparent 70%),
      linear-gradient(90deg, #0a2f9c 0%, #0c3fb8 30%, #0b2f9a 60%, #0a35ad 100%);
    overflow: hidden;
    font-family: "Montserrat", sans-serif;
    color: var(--white);
  }
  .tech-backdrop {
    position: absolute; left: 0; top: 82px; width: 100%; height: 367px;
    background:
      linear-gradient(90deg, rgba(90,180,255,.25), transparent 25%, transparent 75%, rgba(90,180,255,.25)),
      radial-gradient(ellipse 60% 40% at 50% 55%, rgba(60,140,255,.25), transparent 70%);
  }
  .header {
    position: absolute; left: 0; top: 0; width: 100%; height: 82px;
    display: flex; align-items: center;
  }
  .brand {
    position: absolute; left: 62px; top: 20px;
    display: flex; align-items: center; gap: 12px;
  }
  .brand-dot {
    width: 22px; height: 22px; border-radius: 50%; background: var(--white);
  }
  .brand-name {
    font-weight: 800; font-size: 46px; letter-spacing: .5px; line-height: 1;
  }
  .tagline {
    position: absolute; left: 389px; top: 32px;
    font-family: "Barlow Semi Condensed", sans-serif;
    font-weight: 700; font-size: 34px; line-height: 1; letter-spacing: .3px;
  }
  .header-rule {
    position: absolute; left: 389px; right: 170px; top: 82px; height: 2px;
    background: linear-gradient(90deg, rgba(127,208,255,.9), rgba(127,208,255,.2));
  }
  .offer {
    position: absolute; left: 180px; top: 105px; width: 600px; text-align: center;
  }
  .price {
    font-weight: 900; font-size: 140px; line-height: 1; letter-spacing: -4px;
    color: var(--price-yellow);
  }
  .offer-rule {
    width: 540px; height: 2px; margin: 16px auto 0;
    background: linear-gradient(90deg, transparent, var(--cyan), transparent);
  }
  .features {
    margin-top: 22px; font-weight: 800; font-size: 37px; line-height: 1;
  }
  .features .plus { color: var(--price-yellow); }
  .features .unit { font-size: 26px; }
  .calls {
    margin-top: 16px; font-weight: 800; font-size: 31px; line-height: 1;
  }
  .globe {
    position: absolute; left: 790px; top: 113px; width: 294px; height: 294px;
    border-radius: 50%;
    background: radial-gradient(circle at 38% 35%, #5db8ff 0%, #1d62d8 45%, #0a2f9a 80%, #0b2a80 100%);
    box-shadow: 0 0 60px rgba(90,180,255,.8);
  }
  .contact-band {
    position: absolute; left: 0; bottom: 0; width: 100%; height: 78px;
    background: var(--band-blue);
    border-top: 2px solid rgba(160,200,255,.7);
  }
  .phone {
    position: absolute; left: 158px; top: 16px;
    display: flex; align-items: center; gap: 12px;
    font-weight: 800; font-size: 42px; line-height: 1;
  }
  .phone svg { width: 40px; height: 40px; }
  .website {
    position: absolute; right: 154px; top: 16px;
    font-weight: 800; font-size: 42px; line-height: 1;
  }
</style>
</head>
<body>
<div class="canvas">
  <section class="billboard">
    <div class="tech-backdrop" role="img" aria-label="Fondo tecnológico de líneas de luz y circuitos en tonos azules"></div>

    <header class="header">
      <div class="brand">
        <span class="brand-dot"></span>
        <span class="brand-name">LUMA</span>
      </div>
      <h1 class="tagline">INTERNET ULTRARRÁPIDO EN TU ZONA</h1>
    </header>
    <div class="header-rule"></div>

    <div class="offer">
      <p class="price">29,90€</p>
      <div class="offer-rule"></div>
      <p class="features">1000 MEGAS <span class="plus">+</span> 100<span class="unit">GB</span> MÓVIL</p>
      <p class="calls">LLAMADAS ILIMITADAS</p>
    </div>

    <div class="globe" role="img" aria-label="Globo terrestre luminoso con red de conexiones"></div>

    <footer class="contact-band">
      <div class="phone">
        <svg viewBox="0 0 24 24" aria-hidden="true"><path fill="#ffffff" d="M6.6 10.8a15.1 15.1 0 0 0 6.6 6.6l2.2-2.2a1 1 0 0 1 1-.25 11.4 11.4 0 0 0 3.6.57 1 1 0 0 1 1 1V20a1 1 0 0 1-1 1A17 17 0 0 1 3 4a1 1 0 0 1 1-1h3.5a1 1 0 0 1 1 1c0 1.25.2 2.46.57 3.6a1 1 0 0 1-.25 1z"/></svg>
        <span>956 47 8092</span>
      </div>
      <div class="website">lu-ma.es</div>
    </footer>
  </section>
</div>
</body>
</html>
```